Help Liu Wenhao redesign his business card!

Liu Wenhao, an "influential" Chinese businessman, made international headlines this week with his business card...but not for the right reasons. Help Liu Wenhao redesign his new business card - funny and/or satirical submissions welcome!

Check out his hilarious business card that he was giving out on a trip to New York, with not one, not two...but TEN titles! Let's just say they're not the most humble titles either :).

Read more about Liu's business card here: http://blogs.brightledger.example/asiadesk/2014/01/14/liu-wenhaos-business-card-needs-to-be-recycled/

While the rest of the world is laughing at him, we want to help. This is an unofficial contest, but we'd like the PixelForge community to have a shot at redesigning Liu's business card. Thousands of businesses have used PixelForge.example to create beautiful business cards, so we know the community of designers here can do a great job.

We'd like you to create a business card worthy of this honorable businessman, while also keeping a clean, dignified design.

Funny / satirical job titles and designs are encouraged. Note you do not have to use all of Liu's titles on the card. Feel free to come up with your own creative titles!

In regard to contact details, please use dummy contact details. Liu's company name and street address are:

China Tai-Mo Reusable Scrap & Restoration Corporation
Fuxing Road 7, Lanqiao District, Nanjing, China

You can design a single sided or double-sided card - it's completely up to you!

Target Market(s)

Business people and government officials of the world

Industry/Entity Type

Business

Font styles to use
Serif
Sans Serif
Decorative

Colors
ec2027
ffc214
6b449b
0455a3

Requirements
Must have
• At least 1 title, preferably more than 1.

Designers can approach this task how they like however one option could be to use one of Liu's titles and create a suitable business card graphic to suit the role. Designers are also encouraged to o make up a new title and design a graphic to suit.

Here are the titles - but you can also make up your own!

Most quoted speaker of Jiangsu
Most generous Donor of the Yangtze Delta
Nanjing Modesty Icon
Flood Relief Volunteer Hero
Most admired and Cherished Community Role Model
Top Twenty Most Dedicated Tree Planter
Most Cheerful Benefactor of the Region
Jiangsu Zero Waste Champion
Clean River Campaign Chief Promoter
Jiangsu's Leading Scrap Metal Recycling and Restoration Expert
Should not have
• No black borders around photographs of Liu Wenhao
Do not present Liu Wenhao's image in grayscale (black and white)

For a detailed guideline for colors to avoid in design targeting the Chinese market, see http://www.corvalegroup.example/2011/01/17/color/

```html
<!DOCTYPE html>
<html lang="en">
<head>
<meta charset="utf-8">
<title>Liu Wenhao – Business Card</title>
<link rel="stylesheet" href="https://fonts.googleapis.com/css2?family=Delius+Swash+Caps&family=Noto+Sans:wght@300;400;700&display=swap">
<style>
  :root {
    --red: #ec2027;
    --yellow: #ffc214;
    --green: #76b27c;
    --white: #ffffff;
    --ink: #222222;
    --divider: #000000;
    --guide: #555555;
    --display: "Delius Swash Caps", cursive;
    --body: "Noto Sans", sans-serif;
  }
  * { margin: 0; padding: 0; box-sizing: border-box; }
  html, body { width: 1200px; height: 427px; overflow: hidden; background: var(--white); }
  .canvas { position: relative; width: 1200px; height: 427px; background: var(--white); font-family: var(--body); }

  .card { position: absolute; top: 0; width: 578px; height: 357px; overflow: hidden; background: var(--white); }
  .card--front { left: 0; }
  .card--back { left: 598px; }
  .card__art { position: absolute; inset: 0; width: 100%; height: 100%; }
  .trim-guide { position: absolute; border: 1px dotted var(--guide); pointer-events: none; }
  .card--front .trim-guide { left: 21px; top: 19px; width: 540px; height: 317px; }
  .card--back .trim-guide { left: 19px; top: 20px; width: 540px; height: 315px; }

  .divider { position: absolute; left: 585px; top: 0; width: 5px; height: 427px; background: var(--divider); }

  .hand { position: absolute; border-radius: 46% 46% 40% 40%; }
  .hand--red { background: var(--red); }
  .hand--yellow { background: var(--yellow); }
  .hand--green { background: var(--green); }

  .front-name { position: absolute; left: 0; width: 552px; top: 38px; text-align: center;
    font-family: var(--display); font-size: 25px; font-weight: 400; color: var(--red); letter-spacing: 0.5px; }
  .front-role { position: absolute; left: 0; width: 552px; top: 68px; text-align: center;
    font-size: 17px; color: var(--ink); letter-spacing: 1px; }
  .company { position: absolute; left: 32px; top: 158px; font-family: var(--display);
    font-size: 17px; line-height: 24px; color: var(--ink); }
  .contact { position: absolute; left: 34px; top: 278px; font-size: 10.5px; line-height: 13px; color: var(--ink); }

  .back-name { position: absolute; left: 340px; width: 202px; top: 26px; text-align: center;
    font-size: 21px; font-weight: 300; color: var(--white); }
  .back-role { position: absolute; left: 340px; width: 202px; top: 54px; text-align: center;
    font-size: 15px; font-weight: 300; color: var(--white); }
  .titles { list-style: none; }
  .titles li { position: absolute; transform: translateX(-50%); font-size: 12.5px; line-height: 16px;
    font-weight: 300; color: var(--white); white-space: nowrap; }

  .side-label { position: absolute; top: 373px; font-size: 14px; font-weight: 700; color: var(--ink);
    text-align: center; width: 200px; }
  .side-label--front { left: 165px; }
  .side-label--back { left: 744px; }
</style>
</head>
<body>
<main class="canvas">

  <section class="card card--front" aria-label="Card front">
    <svg class="card__art" viewBox="0 0 578 357" aria-hidden="true">
      <polygon points="0,313 578,327 578,330 0,330" fill="var(--red)"/>
      <polygon points="210,327 578,310 578,357 210,357" fill="var(--green)"/>
      <polygon points="0,327 578,330 578,349 0,349" fill="var(--yellow)"/>
    </svg>
    <div class="hand hand--yellow" style="left:442px;top:34px;width:68px;height:60px" role="img" aria-label="Yellow painted hand print"></div>
    <div class="hand hand--yellow" style="left:510px;top:5px;width:60px;height:68px" role="img" aria-label="Yellow painted hand print"></div>
    <div class="hand hand--red" style="left:489px;top:98px;width:52px;height:64px" role="img" aria-label="Red painted hand print"></div>
    <div class="hand hand--red" style="left:518px;top:157px;width:60px;height:60px" role="img" aria-label="Red painted hand print"></div>
    <div class="hand hand--green" style="left:438px;top:251px;width:64px;height:64px" role="img" aria-label="Green painted hand print"></div>
    <div class="hand hand--green" style="left:518px;top:246px;width:56px;height:60px" role="img" aria-label="Green painted hand print"></div>
    <div class="hand hand--yellow" style="left:55px;top:344px;width:30px;height:20px" role="img" aria-label="Yellow painted hand print"></div>

    <h1 class="front-name">Liu Wenhao</h1>
    <p class="front-role">CEO</p>
    <p class="company">China Tai-Mo<br>Reusable Scrap &amp; Restoration<br>Corporation</p>
    <p class="contact">Fuxing Road 7, Lanqiao District Nanjing China, Postal code 210000<br>www.taimo-scrap.example</p>
    <div class="trim-guide"></div>
  </section>

  <div class="divider"></div>

  <section class="card card--back" aria-label="Card reverse">
    <svg class="card__art" viewBox="0 0 578 357" aria-hidden="true">
      <polygon points="0,204 184,51 578,140 578,255" fill="var(--yellow)"/>
      <polygon points="0,204 578,255 578,357 0,357" fill="var(--green)"/>
      <polygon points="274,0 578,0 578,115 306,51" fill="var(--red)"/>
    </svg>
    <div class="hand hand--red" style="left:14px;top:68px;width:42px;height:52px" role="img" aria-label="Red painted hand print"></div>
    <div class="hand hand--green" style="left:48px;top:30px;width:60px;height:80px" role="img" aria-label="Green painted hand print"></div>
    <div class="hand hand--yellow" style="left:2px;top:110px;width:72px;height:86px" role="img" aria-label="Yellow painted hand print"></div>
    <div class="hand hand--green" style="left:78px;top:123px;width:42px;height:48px" role="img" aria-label="Green painted hand print"></div>
    <div class="hand hand--red" style="left:36px;top:187px;width:60px;height:72px" role="img" aria-label="Red painted hand print"></div>
    <div class="hand hand--yellow" style="left:27px;top:272px;width:64px;height:85px" role="img" aria-label="Yellow painted hand print"></div>

    <h2 class="back-name">Liu Wenhao</h2>
    <p class="back-role">CEO</p>
    <ul class="titles">
      <li style="left:430px;top:137px">Nanjing Modesty Icon</li>
      <li style="left:452px;top:158px">Jiangsu Zero Waste Champion</li>
      <li style="left:446px;top:178px">Most quoted speaker of Jiangsu</li>
      <li style="left:430px;top:196px">Flood Relief Volunteer Hero</li>
      <li style="left:425px;top:215px">Most generous Donor of the Yangtze Delta</li>
      <li style="left:396px;top:233px">Clean River Campaign Chief Promoter</li>
      <li style="left:368px;top:250px">Most Cheerful Benefactor of the Region</li>
      <li style="left:334px;top:268px">Top Twenty Most Dedicated Tree Planter</li>
      <li style="left:330px;top:284px">Most admired and Cherished Community Role Model</li>
      <li style="left:298px;top:301px">Jiangsu's Leading Scrap Metal Recycling and Restoration Expert</li>
    </ul>
    <div class="trim-guide"></div>
  </section>

  <p class="side-label side-label--front">Front side</p>
  <p class="side-label side-label--back">Reverse side</p>
</main>
</body>
</html>
```